Vorna Fleet business card

I am needing a business card that at a glance shows all the services that we provide emphasizing some more than others. We are a Fleet and Compliance management company as well as a software company. We provide outsourced solutions for KPX compliance and HR services via our own software.
In addition, we do
drug testing
GPS
Cameras
Electronic DVIRS
ELD's

Target Market(s)

Transportation company owners

Industry/Entity Type

Transportation supplier

Contact Information for Business Card

the card should inform potential customers what we do

Other font styles liked:
• I have added brand guidelines. See attached

Requirements
Must have
• See description
Should not have
• Colors outside my brand guide. See attached

```html
<!DOCTYPE html>
<html lang="en">
<head>
<meta charset="utf-8">
<title>Vorna Fleet business card</title>
<link rel="stylesheet" href="https://fonts.googleapis.com/css2?family=Open+Sans:wght@400;600;700;800&display=swap">
<style>
  :root {
    --bg: #e9e6e1;
    --card: #ffffff;
    --ink: #1b1b1b;
    --ink-soft: #2a2a2a;
    --brand-red: #e8202a;
    --band-dark: #1e1e1e;
    --shadow: rgba(0, 0, 0, 0.18);
  }
  * { box-sizing: border-box; margin: 0; padding: 0; }
  html, body {
    width: 1200px; height: 900px; overflow: hidden;
    background: var(--bg);
    font-family: "Open Sans", Arial, sans-serif;
    color: var(--ink);
  }
  .stage { position: relative; width: 1200px; height: 900px; }
  .card {
    position: absolute;
    width: 640px; height: 366px;
    background: var(--card);
    box-shadow: 0 8px 24px var(--shadow);
    overflow: hidden;
  }

  /* front */
  .card-front { left: 180px; top: 56px; }
  .front-lockup {
    position: absolute; left: 0; right: 0; top: 104px;
    display: flex; flex-direction: column; align-items: center;
  }
  .front-wordmark { display: flex; align-items: center; gap: 18px; }
  .mark-square { width: 40px; height: 40px; background: var(--brand-red); flex: none; }
  .wordmark-text {
    font-weight: 800; font-size: 64px; line-height: 1; letter-spacing: 1px; color: var(--ink);
  }
  .services-lead {
    margin-top: 26px;
    font-weight: 700; font-size: 17px; letter-spacing: 4px;
    text-transform: uppercase; color: var(--brand-red);
  }
  .services-list {
    margin-top: 10px;
    font-weight: 600; font-size: 14px; letter-spacing: 2px;
    text-transform: uppercase; color: var(--ink-soft);
  }

  /* back */
  .card-back { left: 380px; top: 478px; }
  .back-wordmark {
    position: absolute; left: 40px; top: 40px;
    display: flex; align-items: center; gap: 10px;
  }
  .back-wordmark .mark-square { width: 22px; height: 22px; }
  .back-wordmark .wordmark-text { font-size: 36px; }
  .contact-list {
    position: absolute; left: 44px; top: 118px;
    list-style: none;
  }
  .contact-item {
    display: flex; align-items: center; gap: 16px;
    font-size: 16px; font-weight: 400; color: var(--ink-soft);
    height: 32px;
  }
  .contact-icon { width: 20px; height: 20px; flex: none; }
  .holder {
    position: absolute; right: 40px; top: 148px; text-align: right;
  }
  .holder-name { font-weight: 700; font-size: 26px; line-height: 1.1; color: var(--ink); }
  .holder-role { font-weight: 400; font-size: 21px; line-height: 1.2; color: var(--ink); }
  .base-band { position: absolute; left: 0; bottom: 0; width: 640px; height: 80px; }
</style>
</head>
<body>
<main class="stage">

  <section class="card card-front" aria-label="Card front">
    <div class="front-lockup">
      <div class="front-wordmark">
        <span class="mark-square"></span>
        <span class="wordmark-text">Vorna Fleet</span>
      </div>
      <p class="services-lead">KPX Compliance · HR Software</p>
      <p class="services-list">Drug Testing · GPS · Cameras · eDVIRs · ELDs</p>
    </div>
  </section>

  <section class="card card-back" aria-label="Card back">
    <div class="back-wordmark">
      <span class="mark-square"></span>
      <span class="wordmark-text">Vorna Fleet</span>
    </div>

    <ul class="contact-list">
      <li class="contact-item">
        <svg class="contact-icon" viewBox="0 0 20 20" fill="none" stroke="#e8202a" stroke-width="1.6">
          <rect x="1" y="1" width="18" height="18" rx="2"/>
          <path d="M6 5l2 0 1 3-1.4 1a6 6 0 0 0 3.4 3.4l1-1.4 3 1v2c-4.5.5-9.5-4.5-9-9z" fill="#e8202a" stroke="none"/>
        </svg>
        <span>416-555-0182</span>
      </li>
      <li class="contact-item">
        <svg class="contact-icon" viewBox="0 0 20 20" fill="none" stroke="#e8202a" stroke-width="1.6">
          <rect x="1" y="1" width="18" height="18" rx="2"/>
          <rect x="6.5" y="4.5" width="7" height="11" rx="1"/>
        </svg>
        <span>(02) 5550 417</span>
      </li>
      <li class="contact-item">
        <svg class="contact-icon" viewBox="0 0 20 20" fill="none" stroke="#e8202a" stroke-width="1.6">
          <rect x="1" y="1" width="18" height="18" rx="2"/>
          <path d="M4 10l6-5 6 5M6 9v6h8V9"/>
        </svg>
        <span>Your Address</span>
      </li>
      <li class="contact-item">
        <svg class="contact-icon" viewBox="0 0 20 20" fill="none" stroke="#e8202a" stroke-width="1.6">
          <rect x="1" y="1" width="18" height="18" rx="2"/>
          <rect x="4.5" y="6" width="11" height="8"/>
          <path d="M4.5 6l5.5 4.5L15.5 6"/>
        </svg>
        <span>youremail@vornamail.com</span>
      </li>
      <li class="contact-item">
        <svg class="contact-icon" viewBox="0 0 20 20" fill="none" stroke="#e8202a" stroke-width="1.6">
          <rect x="1" y="1" width="18" height="18" rx="2"/>
          <circle cx="10" cy="10" r="5"/>
          <path d="M5 10h10M10 5c-2.5 3-2.5 7 0 10M10 5c2.5 3 2.5 7 0 10"/>
        </svg>
        <span>youremail@website.com</span>
      </li>
      <li class="contact-item">
        <svg class="contact-icon" viewBox="0 0 20 20" fill="none" stroke="#e8202a" stroke-width="1.6">
          <rect x="1" y="1" width="18" height="18" rx="2"/>
          <path d="M10 15s-5-3.2-5-6.2A2.6 2.6 0 0 1 10 7.4a2.6 2.6 0 0 1 5 1.4c0 3-5 6.2-5 6.2z" fill="#e8202a" stroke="none"/>
        </svg>
        <span>www.yourwebsite.com</span>
      </li>
    </ul>

    <div class="holder">
      <p class="holder-name">Dana Whitford</p>
      <p class="holder-role">Director</p>
    </div>

    <svg class="base-band" viewBox="0 0 640 80" preserveAspectRatio="none" aria-hidden="true">
      <path d="M0 68 H360 C378 68 382 40 400 40 H640 V80 H0 Z" fill="#e8202a"/>
      <path d="M0 74 H364 C382 74 388 46 406 46 H640 V80 H0 Z" fill="#1e1e1e"/>
      <rect x="0" y="74" width="370" height="6" fill="#e8202a"/>
    </svg>
  </section>

</main>
</body>
</html>
```